Paper and board wholesaler needs business card design for managers

We need a business card design that incorporates bordo red, white and/ or grey colors. The business card has to have our "VELON" logo and our partners paper group logo that we are part of - "ROSKU group". Both of the logos should be applied to the business card according to the guidelines for the usage of the logo that have been added in the uploaded files.
The letters (information on the card) should be easily readable, so no "shiny" or "glossy" text.
Besides the two logos, the business card needs to contain information for the respective person:
1) Name, Surname,
2) Job position (e.g. "sales represantative"),
3) E-mail,
4) Phone number,
5) text: "Kartonu Mājvieta (VELON)" LTD
6) our office address "Riga, Sārtaines street 42".
(also could have) 7) our homepage address "www.velon.lv"
Holiday season, so have a lot of tasks to take care of and not as much time to check SketchHarbor as often.
1) Name, Surname, 2) Job position (e.g. "sales represantative"), 3) E-mail, 4) Phone number, 5) text: "Kartonu Mājvieta (VELON)" LTD 6) our office address "Riga, Sārtaines street 42". (also could have) 7) our homepage address "www.velon.lv"
Other font styles liked:
- Josefin Sans

```html
<!DOCTYPE html>
<html lang="en">
<head>
<meta charset="utf-8">
<title>VELON business card</title>
<link rel="stylesheet" href="https://fonts.googleapis.com/css2?family=Montserrat:wght@400;500;700&display=swap">
<style>
:root{
  --bordo:#7f2c33;
  --ink:#1e1e1e;
  --charcoal:#2a2a2a;
  --paper:#ffffff;
  --stage:#3b3b3b;
  --logo-grey:#6c6c6c;
  --mark-dark:#1c1c1c;
}
*{margin:0;padding:0;box-sizing:border-box}
html,body{width:1200px;height:1059px;overflow:hidden}
body{background:var(--stage);position:relative;font-family:"Montserrat",sans-serif}
.card{position:absolute;width:688px;height:391px;border-radius:18px;overflow:hidden}
.card-front{left:256px;top:100px;background:var(--paper)}
.card-back{left:253px;top:537px;width:694px;height:394px;background:var(--charcoal)}
.wave{position:absolute;left:0;top:0;width:688px;height:391px}
.brand{position:absolute;display:flex;align-items:center}
.brand-square{border:2px solid var(--bordo);flex:none}
.brand-name{font-weight:500;color:var(--bordo);white-space:nowrap}
.front-brand{left:92px;top:152px}
.front-brand .brand-square{width:42px;height:54px;margin-right:33px}
.front-brand .brand-name{font-size:20px;letter-spacing:21px;margin-right:-21px}
.divider{position:absolute;left:346px;top:94px;width:1.5px;height:170px;background:var(--bordo)}
.person{position:absolute;left:372px;top:90px}
.person-name{font-size:30px;font-weight:700;color:var(--bordo);letter-spacing:.5px;line-height:1.1}
.person-role{font-size:17px;color:var(--ink);margin-top:1px}
.contacts{position:absolute;left:372px;top:171px;list-style:none}
.contacts li{display:flex;align-items:center;height:25px;font-size:16px;color:var(--ink)}
.contacts svg{width:13px;height:13px;margin-right:8px;fill:var(--bordo);flex:none}
.back-brand{left:139px;top:147px}
.back-brand .brand-square{width:74px;height:100px;border:3px solid var(--mark-dark);margin-right:62px}
.back-brand .brand-name{font-size:40px;letter-spacing:36px;margin-right:-36px;color:var(--logo-grey)}
.company{position:absolute;left:0;right:0;top:333px;text-align:center;font-size:17px;color:#f2f2f2;letter-spacing:.5px}
</style>
</head>
<body>
<section class="card card-front">
  <svg class="wave" viewBox="0 0 688 391" aria-hidden="true">
    <path d="M0 305 C60 345 140 368 260 366 C380 364 480 310 600 304 C640 302 670 318 688 335 L688 391 L0 391 Z" fill="var(--bordo)"/>
    <path d="M0 311 C60 350 140 372 260 370 C380 368 480 325 600 322 C640 322 670 336 688 355 L688 391 L0 391 Z" fill="var(--paper)"/>
    <path d="M0 313 C60 352 140 374 260 372 C380 370 480 328 600 325 C640 325 670 339 688 358 L688 391 L0 391 Z" fill="var(--charcoal)"/>
  </svg>
  <div class="brand front-brand"><span class="brand-square"></span><span class="brand-name">VELON</span></div>
  <div class="divider"></div>
  <div class="person">
    <h1 class="person-name">JANIS OZOLS</h1>
    <p class="person-role">Sales Represantative</p>
  </div>
  <ul class="contacts">
    <li><svg viewBox="0 0 24 24"><path d="M6.6 10.8a15.1 15.1 0 0 0 6.6 6.6l2.2-2.2c.3-.3.7-.4 1-.2 1.1.4 2.3.6 3.6.6.6 0 1 .4 1 1V20c0 .6-.4 1-1 1A17 17 0 0 1 3 4c0-.6.4-1 1-1h3.5c.6 0 1 .4 1 1 0 1.3.2 2.5.6 3.6.1.3 0 .7-.2 1z"/></svg>123-456-7890</li>
    <li><svg viewBox="0 0 24 24"><path d="M2 5h20v2l-10 6L2 7z M2 9l10 6 10-6v10H2z"/></svg>info@velon.lv</li>
    <li><svg viewBox="0 0 24 24"><path d="M12 2a10 10 0 1 0 0 20 10 10 0 0 0 0-20zm7.9 9h-3.9a15 15 0 0 0-1.4-6.4A8 8 0 0 1 19.9 11zM12 4c1 1.3 1.9 3.9 2 7h-4c.1-3.1 1-5.7 2-7zM9.4 4.6A15 15 0 0 0 8 11H4.1a8 8 0 0 1 5.3-6.4zM4.1 13H8a15 15 0 0 0 1.4 6.4A8 8 0 0 1 4.1 13zM12 20c-1-1.3-1.9-3.9-2-7h4c-.1 3.1-1 5.7-2 7zm2.6-.6A15 15 0 0 0 16 13h3.9a8 8 0 0 1-5.3 6.4z"/></svg>www.velon.lv</li>
    <li><svg viewBox="0 0 24 24"><path d="M12 2a7 7 0 0 0-7 7c0 5 7 13 7 13s7-8 7-13a7 7 0 0 0-7-7zm0 9.5A2.5 2.5 0 1 1 12 6.5a2.5 2.5 0 0 1 0 5z"/></svg>Riga, Sārtaines street 42</li>
  </ul>
</section>
<section class="card card-back">
  <div class="brand back-brand"><span class="brand-square"></span><span class="brand-name">VELON</span></div>
  <p class="company">Kartonu Mājvieta (VELON)" LTD</p>
</section>
</body>
</html>
```